Comprehensive guide for the front desk medical office staff.

selling a reference guide for the front desk personnel at Urgent Care clinics

Target Market(s)

Urgent Care and physian office manager s

Industry/Entity Type

Medical

```html
<!DOCTYPE html>
<html lang="en">
<head>
<meta charset="utf-8">
<title>Front Desk Reference Guide – Poster</title>
<link href="https://fonts.googleapis.com/css2?family=Roboto+Condensed:ital,wght@0,400;0,500;0,700;1,500;1,700&display=swap" rel="stylesheet">
<style>
  :root {
    --navy: #06344f;
    --sky: #3db0e6;
    --sun: #fcd307;
    --alert: #e4432d;
    --white: #ffffff;
    --backdrop: #e6e8ea;
  }
  html, body {
    margin: 0;
    padding: 0;
    width: 1200px;
    height: 1200px;
    overflow: hidden;
    background: var(--backdrop);
  }
  .canvas {
    position: relative;
    width: 1200px;
    height: 1200px;
  }
  .poster {
    position: absolute;
    left: 197px;
    top: 3px;
    width: 806px;
    height: 1193px;
    background: var(--navy);
    overflow: hidden;
    font-family: "Roboto Condensed", "Arial Narrow", sans-serif;
    color: var(--white);
  }
  .shapes {
    position: absolute;
    inset: 0;
  }
  .text-block {
    position: absolute;
    left: 0;
    right: 0;
    text-align: center;
    margin: 0;
  }
  .author {
    top: 46px;
    font-size: 31px;
    font-weight: 700;
  }
  .kicker {
    top: 100px;
    font-size: 37px;
    font-weight: 700;
    color: var(--sun);
  }
  .title {
    top: 150px;
    font-size: 69px;
    font-weight: 700;
    line-height: 61px;
    color: var(--sky);
  }
  .subtitle {
    top: 279px;
    font-size: 28px;
    font-weight: 500;
    line-height: 41px;
    color: var(--sky);
  }
  .info-card {
    position: absolute;
    left: 170px;
    top: 507px;
    width: 184px;
    height: 250px;
    background: var(--navy);
    text-align: center;
    box-shadow: 2px 3px 0 rgba(255,255,255,0.8);
  }
  .info-card__label {
    margin: 22px 0 0;
    font-size: 21px;
    font-weight: 500;
    line-height: 25px;
    color: var(--sun);
  }
  .info-card__name {
    margin: 16px 0 0;
    font-size: 23px;
    font-weight: 500;
    font-style: italic;
  }
  .info-card__body {
    margin: 6px 0 0;
    font-size: 16.5px;
    line-height: 22px;
  }
  .buy-button {
    position: absolute;
    left: 165px;
    top: 791px;
    width: 186px;
    height: 45px;
    background: var(--alert);
    color: var(--white);
    font-size: 31px;
    font-weight: 700;
    font-style: italic;
    line-height: 45px;
    text-align: center;
  }
  .benefits {
    position: absolute;
    left: 93px;
    top: 897px;
    margin: 0;
    padding: 0;
    list-style: none;
    font-size: 26px;
    font-weight: 500;
    line-height: 32.5px;
  }
  .benefits li {
    display: flex;
    align-items: center;
    gap: 10px;
  }
  .benefits svg {
    width: 26px;
    height: 22px;
    flex: none;
  }
  .order {
    top: 1043px;
    font-size: 59px;
    font-weight: 700;
    line-height: 66px;
  }
  .price {
    top: 1104px;
    font-size: 31px;
    font-weight: 700;
    color: var(--sun);
  }
</style>
</head>
<body>
<div class="canvas">
  <article class="poster">
    <svg class="shapes" viewBox="0 0 806 1193" width="806" height="1193" aria-hidden="true">
      <g stroke="#ffffff" stroke-width="1.6">
        <line x1="105" y1="61" x2="288" y2="61"/>
        <line x1="105" y1="67" x2="288" y2="67"/>
        <line x1="120" y1="73" x2="275" y2="73"/>
        <line x1="527" y1="61" x2="710" y2="61"/>
        <line x1="527" y1="67" x2="710" y2="67"/>
        <line x1="540" y1="73" x2="697" y2="73"/>
      </g>
      <defs>
        <linearGradient id="photoTone" x1="0" y1="0" x2="1" y2="0">
          <stop offset="0" stop-color="#efefef"/>
          <stop offset="0.5" stop-color="#f4f2f0"/>
          <stop offset="0.72" stop-color="#e2c3a6"/>
          <stop offset="1" stop-color="#b88862"/>
        </linearGradient>
      </defs>
      <path role="img" aria-label="Photo of a smiling mother hugging her curly-haired daughter in a bright room"
            d="M0,533 Q400,330 806,437 L806,737 Q450,990 0,835 Z" fill="url(#photoTone)"/>
      <path d="M0,488 Q180,410 350,393 Q170,425 0,533 Z" fill="var(--sun)"/>
      <path d="M430,885 Q650,860 806,737 L806,778 Q650,875 430,885 Z" fill="var(--sun)"/>
    </svg>

    <p class="text-block author">Laura Whitfield</p>
    <p class="text-block kicker">FRONT DESK REFERENCE GUIDE FOR</p>
    <h1 class="text-block title">URGENT CARE CENTERS<br>AND PHYSIAN OFFICES</h1>
    <p class="text-block subtitle">Glossary of medical terminology used by front office<br>medical staff and insurance companies</p>

    <div class="info-card">
      <p class="info-card__label">DESK<br>INSURANCE<br>CARD</p>
      <p class="info-card__name">Laura Whitfield</p>
      <p class="info-card__body">shares over a decade<br>of medical office<br>experience in this<br>comprehensive guide.</p>
    </div>
    <div class="buy-button">BUY NOW</div>

    <ul class="benefits">
      <li><svg viewBox="0 0 26 22" aria-hidden="true"><path d="M2,12 L9,19 L24,3" fill="none" stroke="var(--sun)" stroke-width="4.5" stroke-linecap="round" stroke-linejoin="round"/></svg>Shows staff how to read an insurance card.</li>
      <li><svg viewBox="0 0 26 22" aria-hidden="true"><path d="M2,12 L9,19 L24,3" fill="none" stroke="var(--sun)" stroke-width="4.5" stroke-linecap="round" stroke-linejoin="round"/></svg>What is a deductible and when to collect a copay.</li>
      <li><svg viewBox="0 0 26 22" aria-hidden="true"><path d="M2,12 L9,19 L24,3" fill="none" stroke="var(--sun)" stroke-width="4.5" stroke-linecap="round" stroke-linejoin="round"/></svg>What is Workers comp.</li>
      <li><svg viewBox="0 0 26 22" aria-hidden="true"><path d="M2,12 L9,19 L24,3" fill="none" stroke="var(--sun)" stroke-width="4.5" stroke-linecap="round" stroke-linejoin="round"/></svg>Information in HIPPA guidelines rance plans.</li>
    </ul>

    <p class="text-block order">To order call 555-014-2270</p>
    <p class="text-block price">Price is $99.99 plus $7.00 shipping and handling</p>
  </article>
</div>
</body>
</html>
```